Bluecrest Ore Company needs a company newsletter template

We need a 2-page editable newsletter template, that we can update monthly with various information and pictures. We would like an area to include our values: Be Safe, Be Honest, Be Responsible, Be Respectful, Be Great. Ideally we would have 2-3 bulk text areas to highlight different things each month, with area we an update a picture from time to time and maybe some text areas where we can add a fun fact type thing. Some of the areas we will include are production milestones (if any), monthly tenure, monthly new hires, highlighting an employee that demonstrates our value, community engagement, upcoming holidays/events, press releases. The exact content will likely change month to month but these will be some of the frequent topics. We are a copper Mine in northern Yukon. I've attached our Brand Guidelines and logo files. Our website is ravelorex.com if you want to see the style and type of photos from our site

```html
<!DOCTYPE html>
<html lang="en">
<head>
<meta charset="utf-8">
<title>Bluecrest Ore Company Newsletter – April 2022</title>
<link href="https://fonts.googleapis.com/css2?family=Montserrat:wght@400;500;600;700;800&family=Oswald:wght@600;700&display=swap" rel="stylesheet">
<style>
  :root{
    --brown-dark:#4b2519;
    --brown:#6b3422;
    --sienna:#9c5236;
    --gold:#e3b43c;
    --gold-text:#d9a11c;
    --gold-light:#f0cf72;
    --cream:#fbf3dd;
    --grey-box:#ececec;
    --orange:#f7941d;
    --ink:#2b2b2b;
    --ink-soft:#555555;
    --white:#ffffff;
    --stage:#ffffff;
  }
  *{box-sizing:border-box;margin:0;padding:0}
  html,body{width:806px;height:1200px;overflow:hidden;background:var(--stage)}
  body{font-family:"Montserrat",Arial,sans-serif;color:var(--ink);position:relative}
  .abs{position:absolute}

  /* spread */
  .page{position:absolute;top:315px;width:806px;height:1200px;background:var(--white);overflow:hidden;
    transform:scale(.475);transform-origin:0 0;box-shadow:0 0 14px rgba(0,0,0,.18)}
  .page-front{left:12px}
  .page-back{left:411px}

  /* ---------- page 1 ---------- */
  .brand{left:38px;top:62px;display:flex;align-items:center;gap:10px}
  .brand-mark{width:26px;height:26px;background:var(--gold);flex:none}
  .brand-name{font-weight:700;font-size:21px;color:var(--brown);letter-spacing:.3px;line-height:1.05}
  .masthead{right:45px;top:26px}
  .masthead-title{font-weight:800;font-size:60px;color:var(--brown-dark);letter-spacing:-1px;line-height:1}
  .masthead-issue{font-weight:400;font-size:30px;color:var(--gold-text);letter-spacing:1px;line-height:1;margin-top:2px}

  .hero{left:0;top:148px;width:806px;height:298px;
    background:linear-gradient(160deg,#6a4a36 0%,#8a6446 35%,#a57c58 55%,#6e4c36 80%,#4d3424 100%)}

  .intro{left:41px;top:346px;width:720px;height:244px;background:var(--white)}
  .intro-photo{left:55px;top:356px;width:319px;height:231px;
    background:linear-gradient(180deg,#b9c8d8 0%,#dfe6ee 45%,#eef1f4 70%,#c9ced4 100%)}
  .intro-text{left:388px;top:362px;width:362px}
  .intro-heading{font-weight:700;font-size:21px;color:var(--brown-dark);letter-spacing:-.2px}
  .intro-heading span{color:var(--gold-text)}
  .intro-text p{font-size:12.4px;line-height:15px;margin-top:6px}
  .intro-text .sub{color:var(--gold-text);font-weight:600;font-size:12px;margin-top:7px}

  .month{left:41px;width:436px;height:148px;background:var(--brown-dark);border-radius:4px;display:flex}
  .month-tab{flex:none;width:34px;background:var(--gold);border-radius:4px 0 0 4px;position:relative}
  .month-tab span{position:absolute;left:50%;top:50%;transform:translate(-50%,-50%) rotate(-90deg);
    color:var(--white);font-weight:600;font-size:22px;letter-spacing:.5px;white-space:nowrap}
  .month p{color:var(--white);font-size:11.4px;line-height:14.6px;padding:9px 12px 0 14px}

  .col-heading{display:flex;gap:8px;align-items:flex-start;color:var(--gold-text);font-weight:600;font-size:18.5px;line-height:21px}
  .col-heading svg{flex:none;margin-top:2px}
  .community{left:41px;top:926px;width:270px}
  .community p{font-size:11.6px;line-height:14.6px;margin-top:14px}
  .events{left:334px;top:926px;width:160px}
  .event{margin-top:16px;font-size:13.2px;line-height:16.6px}
  .event b{font-weight:500}
  .event .date{color:var(--sienna)}

  .employee{left:504px;top:718px;width:252px;height:446px;background:var(--sienna);border-radius:0 0 12px 12px}
  .values{left:505px;top:598px}
  .emp-title{left:504px;top:890px;width:252px;text-align:center;font-family:"Oswald",Impact,sans-serif}
  .emp-title .big{font-weight:700;font-size:52px;color:var(--white);line-height:1;letter-spacing:-.5px}
  .emp-title .small{font-weight:600;font-size:27px;color:var(--gold);line-height:1.1;letter-spacing:.5px;text-transform:uppercase}
  .emp-photo{left:552px;top:990px;width:158px;height:130px;
    background:linear-gradient(180deg,#b07a5e 0%,#f2efec 60%,#ffffff 100%);border-radius:6px 6px 0 0}
  .emp-name{left:528px;top:1107px;width:204px;height:44px;background:var(--gold);border-radius:6px;
    color:var(--white);font-size:31px;font-weight:500;text-align:center;line-height:44px;letter-spacing:1px}

  /* ---------- page 2 ---------- */
  .milestone-band{left:522px;top:0;width:284px;height:1100px;background:linear-gradient(180deg,#e9c04a,#e0b236)}
  .press-photo{left:42px;top:39px;width:366px;height:329px;
    background:linear-gradient(180deg,#a9c9e4 0%,#d9dde0 40%,#b7865e 65%,#8a5a38 100%)}
  .press{left:408px;top:39px;width:352px;height:329px;background:var(--brown-dark);border-radius:0 4px 4px 0;padding:16px 22px}
  .press h2{color:var(--gold);font-weight:500;font-size:20px}
  .press p{color:var(--white);font-size:11.9px;line-height:15.6px;margin-top:10px}

  .feature{left:42px;width:458px;background:var(--grey-box)}
  .feature-photo{position:absolute;left:19px;top:19px;width:117px;height:106px}
  .feature-body{position:absolute;left:155px;top:16px;width:290px}
  .feature-body h3{color:var(--gold-text);font-weight:600;font-size:19px}
  .feature-body p{color:var(--ink-soft);font-size:12px;line-height:15.6px;margin-top:2px}

  .fact-text{left:230px;top:732px;width:205px;transform:rotate(-6deg);transform-origin:0 0}
  .fact-text h3{color:var(--brown-dark);font-weight:700;font-size:21px;white-space:nowrap}
  .fact-text p{color:var(--white);font-size:10.8px;line-height:13.6px;margin-top:6px}

  .holidays{display:grid;grid-template-columns:150px 150px;row-gap:8px;margin-top:2px}
  .holiday{font-size:13px;line-height:16px;color:var(--ink)}
  .holiday .date{color:var(--sienna)}
  .holiday small{font-size:12px;color:var(--ink-soft)}

  .milestones-title{left:544px;top:383px;color:var(--brown-dark);font-weight:700;font-size:25px;line-height:30px}
  .milestone{left:541px;width:231px;height:110px;border:2px solid var(--white);display:flex}
  .milestone-year{flex:none;width:44px;background:var(--white);position:relative;
    clip-path:polygon(0 0,100% 0,100% 20%,80% 28%,100% 36%,100% 100%,0 100%)}
  .milestone-year span{position:absolute;left:50%;top:50%;transform:translate(-50%,-50%) rotate(-90deg);
    font-weight:700;font-size:30px;color:var(--brown-dark);letter-spacing:1px}
  .milestone p{color:var(--white);font-size:12.6px;line-height:16px;padding:11px 10px 0 16px;font-weight:500}

  .footer{left:0;top:1100px;width:806px;height:100px;background:linear-gradient(90deg,#6b3422,#8a4a30 50%,#6b3422)}
  .contact{display:flex;align-items:center;gap:7px;color:var(--white);font-size:17px;letter-spacing:.5px}
  .social{display:flex;align-items:center;gap:11px;color:var(--white);font-size:16px}
  .social i{display:block;width:20px;height:20px;border:2px solid var(--gold)}
</style>
</head>
<body>

<article class="page page-front">
  <header>
    <div class="abs brand"><span class="brand-mark"></span><span class="brand-name">BLUECREST ORE<br>COMPANY</span></div>
    <div class="abs masthead">
      <div class="masthead-title">Newsletter</div>
      <div class="masthead-issue">APRIL 2022</div>
    </div>
  </header>

  <div class="abs hero" role="img" aria-label="Aerial photo of the open-pit copper mine with yellow haul trucks and excavators"></div>

  <section>
    <div class="abs intro"></div>
    <div class="abs intro-photo" role="img" aria-label="Photo of mine crew in hard hats and safety gear standing in the snow"></div>
    <div class="abs intro-text">
      <h2 class="intro-heading">OUR PEOPLE. <span>OUR PASSION.</span></h2>
      <p>We strive for sustainability in every aspect of our work. From our environmental practices to community initiatives – we aim to create a positive impact that will last for generations to come.</p>
      <p class="sub">Being a part of the Yukon community</p>
      <p>Community involvement is foundational to Bluecrest. We are proud to partner with the Kestrel River First Nation and invite young adults from Alder Crossing to come and learn about mining. We also partner with Tundra Ridge College and frequently host on-site student tours. Our goal at Bluecrest is to support the community through education, career opportunities, and local and provincial economic development.</p>
    </div>
  </section>

  <section>
    <div class="abs month" style="top:605px">
      <div class="month-tab"><span>JANUARY</span></div>
      <p>Lorem ipsum dolor sit amet, consectetur adipiscing elit, sed do eiusmod tempor incididunt ut labore et dolore magna aliqua. Quis ipsum suspendisse ultrices gravida. Risus commodo viverra maecenas accumsan lacus vel facilisis. Lorem ipsum dolor sit amet, consectetur adipiscing elit, sed do eiusmod tempor incididunt ut labore et dolore magna aliqua. Quis ipsum suspendisse ultrices gravida. Risus commodo viverra maecenas accumsan lacus vel facilisis.</p>
    </div>
    <div class="abs month" style="top:766px">
      <div class="month-tab"><span>FEBRUARY</span></div>
      <p>Lorem ipsum dolor sit amet, consectetur adipiscing elit, sed do eiusmod tempor incididunt ut labore et dolore magna aliqua. Quis ipsum suspendisse ultrices gravida. Risus commodo viverra maecenas accumsan lacus vel facilisis. Lorem ipsum dolor sit amet, consectetur adipiscing elit, sed do eiusmod tempor incididunt ut labore et dolore magna aliqua. Quis ipsum suspendisse ultrices gravida. Risus commodo viverra maecenas accumsan lacus vel facilisis.</p>
    </div>
  </section>

  <section class="abs community">
    <h3 class="col-heading">
      <svg width="28" height="20" viewBox="0 0 28 20" aria-hidden="true"><g fill="var(--brown)"><circle cx="14" cy="5" r="4"/><circle cx="5.5" cy="7" r="3"/><circle cx="22.5" cy="7" r="3"/><path d="M7 19c0-5 3-8 7-8s7 3 7 8z"/><path d="M0 19c0-4 2-7 5.5-7 1.5 0 2.5.5 3 1-1.5 1.5-2.5 3.5-2.5 6z"/><path d="M28 19c0-4-2-7-5.5-7-1.5 0-2.5.5-3 1 1.5 1.5 2.5 3.5 2.5 6z"/></g></svg>
      <span>Community<br>Engagement...</span>
    </h3>
    <p>We're working on extending the mine life by performing definition and step out drilling of known mineralized zones to increase reserves and resources. We're exploring new targets in Bluecrest's large and strategic land package within the Bluecrest Copper Belt. We're exploring new targets in Bluecrest's large and strategic land package within the Bluecrest Copper Belt. In Bluecrest's large and strategic land package within the Bluecrest Copper Belt.</p>
  </section>

  <section class="abs events">
    <h3 class="col-heading">
      <svg width="26" height="24" viewBox="0 0 26 24" aria-hidden="true"><g fill="none" stroke="var(--brown)" stroke-width="2.4"><rect x="2" y="4" width="22" height="18" rx="2"/><path d="M7 1v6M19 1v6M2 10h22"/></g><g fill="var(--brown)"><rect x="6" y="13" width="3.5" height="3"/><rect x="11.3" y="13" width="3.5" height="3"/><rect x="16.5" y="13" width="3.5" height="3"/><rect x="6" y="17.5" width="3.5" height="3"/><rect x="11.3" y="17.5" width="3.5" height="3"/></g></svg>
      <span>Upcoming<br>Events...</span>
    </h3>
    <div class="event"><b>Name of the Event</b><br><span class="date">20th March</span><br>(10.00am-5.00pm)</div>
    <div class="event"><b>Name of the Event</b><br><span class="date">20th March</span><br>(10.00am-5.00pm)</div>
    <div class="event"><b>Name of the Event</b><br><span class="date">20th March</span><br>(10.00am-5.00pm)</div>
  </section>

  <section>
    <div class="abs employee"></div>
    <svg class="abs values" width="250" height="250" viewBox="0 0 250 250" aria-label="Our values: Be Safe, Be Honest, Be Responsible, Be Respectful, Be Great">
      <circle cx="125" cy="125" r="124" fill="var(--cream)"/>
      <circle cx="125" cy="125" r="116" fill="var(--gold)"/>
      <g stroke="var(--cream)" stroke-width="3">
        <line x1="125" y1="125" x2="42" y2="42"/>
        <line x1="125" y1="125" x2="208" y2="42"/>
        <line x1="125" y1="125" x2="10" y2="150"/>
        <line x1="125" y1="125" x2="240" y2="150"/>
        <line x1="125" y1="125" x2="125" y2="241"/>
      </g>
      <circle cx="125" cy="125" r="50" fill="var(--brown)"/>
      <circle cx="125" cy="125" r="43" fill="var(--white)"/>
      <g font-family="Montserrat, Arial, sans-serif" text-anchor="middle" fill="var(--brown-dark)" font-weight="600">
        <text x="125" y="122" font-size="16">OUR</text>
        <text x="125" y="141" font-size="16">VALUES</text>
        <text x="125" y="39" font-size="16">Be</text>
        <text x="125" y="52" font-size="10">Safe</text>
        <text x="40" y="107" font-size="16">Be</text>
        <text x="40" y="120" font-size="10">Great</text>
        <text x="210" y="107" font-size="16">Be</text>
        <text x="210" y="120" font-size="10">Honest</text>
        <text x="82" y="197" font-size="16">Be</text>
        <text x="82" y="210" font-size="10">Respectful</text>
        <text x="168" y="197" font-size="16">Be</text>
        <text x="168" y="210" font-size="10">Responsible</text>
      </g>
    </svg>
    <div class="abs emp-title"><div class="big">EMPLOYEE</div><div class="small">of the year!</div></div>
    <div class="abs emp-photo" role="img" aria-label="Portrait photo of the employee of the year in white shirt and red tie"></div>
    <div class="abs emp-name">JOHN DOE</div>
  </section>
</article>

<article class="page page-back">
  <div class="abs milestone-band"></div>

  <section>
    <div class="abs press-photo" role="img" aria-label="Photo of a dusty wheel loader in front of a crane and ore pile"></div>
    <div class="abs press">
      <h2>Press Releases...</h2>
      <p>Lorem ipsum dolor sit amet, consectetur adipiscing elit, sed do eiusmod tempor incididunt ut labore et dolore magna aliqua. Quis ipsum suspendisse ultrices gravida. Risus commodo viverra maecenas accumsan lacus vel facilisis. Lorem ipsum dolor sit amet, consectetur adipiscing elit, sed do eiusmod tempor incididunt ut labore et dolore magna aliqua. Quis ipsum suspendisse ultrices gravida. Risus commodo viverra maecenas accumsan lacus vel facilisis. Lorem ipsum dolor sit amet, consectetur adipiscing elit, sed do eiusmod tempor incididunt ut labore et dolore magna aliqua. Quis ipsum suspendisse ultrices gravida. Risus commodo viverra maecenas accumsan lacus vel facilisis. Quis ipsum suspendisse ultrices gravida. Risus commodo viverra maecenas accumsan lacus vel facilisis.</p>
    </div>
  </section>

  <section class="abs feature" style="top:388px;height:148px">
    <div class="feature-photo" role="img" aria-label="Photo of a worker beside an excavator on site" style="background:linear-gradient(180deg,#dcd6cf,#a98c6c)"></div>
    <div class="feature-body">
      <h3>Monthly Tenure...</h3>
      <p>Lorem ipsum dolor sit amet, consectetur adipiscing elit, sed do eiusmod tempor incididunt ut labore et dolore magna aliqua. Quis ipsum suspendisse ultrices gravida. Risus commodo viverra maecenas.</p>
    </div>
  </section>

  <section class="abs feature" style="top:552px;height:145px">
    <div class="feature-photo" role="img" aria-label="Photo of two new hires in hard hats and safety vests" style="background:linear-gradient(180deg,#c9d2da,#d9843a)"></div>
    <div class="feature-body">
      <h3>Monthly New Hires...</h3>
      <p>Lorem ipsum dolor sit amet, consectetur adipiscing elit, sed do eiusmod tempor incididunt ut labore et dolore magna aliqua. Quis ipsum suspendisse ultrices gravida.</p>
    </div>
  </section>

  <section>
    <svg class="abs" style="left:72px;top:700px" width="385" height="235" viewBox="0 0 385 235" aria-hidden="true">
      <polygon points="4,36 372,2 382,176 262,186 232,232 226,190 22,210" fill="var(--white)" stroke="#d8d8d8" stroke-width="2"/>
      <polygon points="18,44 362,13 370,166 254,176 234,208 230,180 32,198" fill="var(--orange)"/>
      <polygon points="18,44 150,32 160,188 32,198" fill="#fbb040"/>
    </svg>
    <div class="abs fact-text">
      <h3>DID YOU KNOW?</h3>
      <p>Lorem ipsum dolor sit amet, consectetur adipiscing elit, sed do eiusmod tempor incididunt ut labore et dolore magna aliqua. Quis ipsum suspendisse ultrices gravida. Risus commodo viverra maecenas accumsan lacus vel facilisis.</p>
    </div>
  </section>

  <section class="abs feature" style="top:928px;height:143px">
    <div class="feature-photo" role="img" aria-label="Photo of a straw hat and towel on the beach" style="background:linear-gradient(180deg,#c23a3a,#e8d6b8)"></div>
    <div class="feature-body">
      <h3>Holidays...</h3>
      <div class="holidays">
        <div class="holiday">Holiday<br><span class="date">20th March</span><br><small>(10.00am-5.00pm)</small></div>
        <div class="holiday">Holiday<br><span class="date">20th March</span><br><small>(10.00am-5.00pm)</small></div>
        <div class="holiday">Holiday<br><span class="date">20th March</span><br><small>(10.00am-5.00pm)</small></div>
        <div class="holiday">Holiday<br><span class="date">20th March</span><br><small>(10.00am-5.00pm)</small></div>
      </div>
    </div>
  </section>

  <section>
    <h2 class="abs milestones-title">PRODUCTION<br>MILESTONES</h2>
    <div class="abs milestone" style="top:463px"><div class="milestone-year"><span>2019</span></div><p>Lorem ipsum dolor sit amet, consectetur adipiscing elit, sed do eiusmod tempor incididunt ut labore et dolore magna aliqua.</p></div>
    <div class="abs milestone" style="top:630px"><div class="milestone-year"><span>2020</span></div><p>Lorem ipsum dolor sit amet, consectetur adipiscing elit, sed do eiusmod tempor incididunt ut labore et dolore magna aliqua.</p></div>
    <div class="abs milestone" style="top:795px"><div class="milestone-year"><span>2021</span></div><p>Lorem ipsum dolor sit amet, consectetur adipiscing elit, sed do eiusmod tempor incididunt ut labore et dolore magna aliqua.</p></div>
    <div class="abs milestone" style="top:958px"><div class="milestone-year"><span>2022</span></div><p>Lorem ipsum dolor sit amet, consectetur adipiscing elit, sed do eiusmod tempor incididunt ut labore et dolore magna aliqua.</p></div>
  </section>

  <footer class="abs footer">
    <div class="abs contact" style="left:42px;top:24px">
      <svg width="18" height="18" viewBox="0 0 24 24" aria-hidden="true"><path d="M6.6 10.8a15 15 0 0 0 6.6 6.6l2.2-2.2c.3-.3.7-.4 1-.2 1.1.4 2.3.6 3.6.6.6 0 1 .4 1 1V20c0 .6-.4 1-1 1A17 17 0 0 1 3 4c0-.6.4-1 1-1h3.5c.6 0 1 .4 1 1 0 1.3.2 2.5.6 3.6.1.3 0 .7-.2 1z" fill="none" stroke="var(--gold)" stroke-width="1.8"/></svg>
      <span>(555) 014-2290</span>
    </div>
    <div class="abs contact" style="left:42px;top:56px">
      <svg width="18" height="16" viewBox="0 0 24 20" aria-hidden="true"><g fill="none" stroke="var(--gold)" stroke-width="1.8"><rect x="1.5" y="2" width="21" height="16" rx="2"/><path d="M2 3l10 8 10-8"/></g></svg>
      <span>info@ravelorex.com</span>
    </div>
    <div class="abs contact" style="right:40px;top:24px">
      <svg width="18" height="18" viewBox="0 0 24 24" aria-hidden="true"><g fill="none" stroke="var(--gold)" stroke-width="1.8"><circle cx="12" cy="12" r="10"/><ellipse cx="12" cy="12" rx="4.5" ry="10"/><path d="M2 12h20M4 6.5h16M4 17.5h16"/></g></svg>
      <span>www.ravelorex.com</span>
    </div>
    <div class="abs social" style="right:40px;top:54px">
      <span>Follow Us on</span><i></i><i></i><i></i>
    </div>
  </footer>
</article>

</body>
</html>
```